Company Corporate Profile Brochure for IT Infrastructure Company

Create new corporate profile presentation deck (ie in a format that can be presented in power point) . We are a growing regional IT infrastructure company across Asia Pacific. We need to show case our projects and install abilities for Structure Cabling, Audio Visual and Physical Security (later to lesser extent). I am looking to improve and make look professional the attached current power point. I would like project profile slides that can be customised depending on the country of the prospect. ie If we are bidding a project in the Philippines, we have slides show casing Philippines works, plus our set of high profile projects from other countries. Key Slides for the presentation:-- Company Background- Install Capability + Industry Certifications- Methodology- Project Examples- Key Personnel & Experience- Contact Details.
Target Market(s)
IT Directors, Designers, Real Estate Project Managers
Industry/Entity Type
It Company
Requirements
Must have
- Design in a format that it can be presented as slide presentation.
- About us
- What we do
- Certifications
- Project Profiles
- Key Personnel Profiles

```html
<!DOCTYPE html>
<html lang="en">
<head>
<meta charset="utf-8">
<title>Kestrel Vale — Our Solutions</title>
<link href="https://fonts.googleapis.com/css2?family=Poppins:wght@300;400;600&display=swap" rel="stylesheet">
<style>
  :root{
    --page-bg:#eeeeee;
    --slide-bg:#ffffff;
    --navy:#223248;
    --heading:#23324a;
    --teal:#0f8a6b;
    --sage:#82b77e;
    --white:#ffffff;
    --photo-dark:#0a1a2e;
    --photo-mid:#1d4a78;
    --photo-light:#7fb0db;
  }
  *{margin:0;padding:0;box-sizing:border-box}
  html,body{width:1200px;height:1200px;overflow:hidden;background:var(--page-bg);font-family:"Poppins",sans-serif}
  .slide{position:absolute;left:95px;top:316px;width:1010px;height:568px;background:var(--slide-bg);overflow:hidden}
  .hero-photo{position:absolute;left:0;top:0;width:505px;height:568px;
    background:
      radial-gradient(ellipse at 75% 35%, rgba(127,176,219,.55), transparent 55%),
      linear-gradient(100deg,var(--photo-dark) 0%,var(--photo-mid) 55%,var(--photo-light) 100%)}
  .brand{position:absolute;left:556px;top:36px;font-size:30px;font-weight:400;letter-spacing:1px;color:var(--navy);line-height:1}
  .section-title{position:absolute;left:556px;top:97px;font-size:19px;font-weight:600;color:var(--heading)}
  .accent-dash{position:absolute;left:556px;top:167px;width:19px;height:4px;background:var(--sage)}
  .solutions{position:absolute;left:165px;top:200px;display:flex;height:295px}
  .solution{width:260px;height:100%;color:var(--white);text-align:center;padding-top:25px}
  .solution--it{background:var(--teal)}
  .solution--av{background:var(--sage)}
  .solution--security{background:var(--navy)}
  .solution-icon{display:block;margin:0 auto;width:54px;height:42px}
  .solution-name{margin-top:31px;font-size:13px;font-weight:600}
  .solution-list{list-style:none;margin-top:9px;font-size:11px;font-weight:300;line-height:20px}
  .footer-url{position:absolute;left:826px;top:523px;font-size:11px;font-weight:400;color:var(--teal)}
  .page-number{position:absolute;left:962px;top:522px;font-size:12px;color:var(--heading)}
</style>
</head>
<body>
<main class="slide">
  <div class="hero-photo" role="img" aria-label="Photo of an engineer inspecting server racks in a data centre"></div>

  <div class="brand">KESTRELVALE</div>
  <h1 class="section-title">Our Solutions</h1>
  <div class="accent-dash"></div>

  <section class="solutions">
    <article class="solution solution--it">
      <svg class="solution-icon" viewBox="0 0 54 42" aria-hidden="true">
        <rect width="54" height="42" rx="2" fill="#fff"/>
        <rect y="7" width="54" height="1" fill="var(--teal)"/>
        <circle cx="5" cy="4" r="1" fill="var(--teal)"/><circle cx="9" cy="4" r="1" fill="var(--teal)"/><circle cx="13" cy="4" r="1" fill="var(--teal)"/>
        <circle cx="28" cy="23" r="5" fill="none" stroke="var(--teal)" stroke-width="2"/>
        <line x1="24.5" y1="26.5" x2="21" y2="30" stroke="var(--teal)" stroke-width="2.4" stroke-linecap="round"/>
      </svg>
      <h2 class="solution-name">IT Infrastructure</h2>
      <ul class="solution-list">
        <li>Design</li><li>Fibre &amp; Copper Cabling</li><li>UPS</li><li>Network Equipment</li>
        <li>Network Engineering Services</li><li>Server Room Equipment</li><li>PABX &amp; Telephony Systems</li><li>Wireless</li>
      </ul>
    </article>
    <article class="solution solution--av">
      <svg class="solution-icon" viewBox="0 0 54 42" aria-hidden="true">
        <rect width="54" height="42" rx="2" fill="#fff"/>
        <rect y="7" width="54" height="1" fill="var(--sage)"/>
        <circle cx="5" cy="4" r="1" fill="var(--sage)"/><circle cx="9" cy="4" r="1" fill="var(--sage)"/><circle cx="13" cy="4" r="1" fill="var(--sage)"/>
        <rect x="8" y="17" width="20" height="2" fill="var(--sage)"/><rect x="8" y="23" width="20" height="2" fill="var(--sage)"/><rect x="8" y="29" width="20" height="2" fill="var(--sage)"/>
        <rect x="32" y="17" width="14" height="12" fill="var(--sage)"/><rect x="8" y="34" width="38" height="1.5" fill="var(--sage)"/>
      </svg>
      <h2 class="solution-name">Audio Visual</h2>
      <ul class="solution-list">
        <li>Design</li><li>Display Screens</li><li>Video Conference Solutions</li>
        <li>Meeting Room Control Systems</li><li>Sound Systems</li><li>Audio Cabling</li>
      </ul>
    </article>
    <article class="solution solution--security">
      <svg class="solution-icon" viewBox="0 0 54 42" aria-hidden="true">
        <rect width="54" height="42" rx="2" fill="#fff"/>
        <rect y="7" width="54" height="1" fill="var(--navy)"/>
        <circle cx="5" cy="4" r="1" fill="var(--navy)"/><circle cx="9" cy="4" r="1" fill="var(--navy)"/><circle cx="13" cy="4" r="1" fill="var(--navy)"/>
        <g fill="none" stroke="var(--navy)" stroke-width="2">
          <circle cx="20" cy="21" r="3.5"/><circle cx="35" cy="21" r="3.5"/><circle cx="27" cy="30" r="3.5"/>
          <line x1="22.5" y1="24" x2="25" y2="27"/><line x1="32.5" y1="24" x2="29.5" y2="27"/>
        </g>
      </svg>
      <h2 class="solution-name">Security</h2>
      <ul class="solution-list">
        <li>Design</li><li>Card Access</li><li>CCTV</li><li>Alarm Systems</li>
      </ul>
    </article>
  </section>

  <div class="footer-url">www.yourwebsite.com</div>
  <div class="page-number">3</div>
</main>
</body>
</html>
```